Biz card, letterhead, envelopes for massage business
Massage Business for people and for Equine (horses)
Biz card, letterhead, envelopes for massage business - Massage Therapy
Use same font as used in my logo
simular to my logo
Modern
Marla Kessin
Certified Massage Therapist
P.O. Box 871, Auburn, CA 95718
marlakessin@quillpost.net
I provide massage for people and for horses. We need to creatively put the information on the back of the card. Of course we don't want to say "Human"..... when refering to horse we call it Equine Massage.
Human Massage Therapy.....Swedish, Deep Tissue, Relaxation, Hot Stone, On-Site Chair Massage Equine Massage Therapy...... Stridolan Certified Pellridge Method Relieves muscle pain, enhances performance, reduces inflamation, enhances muscle tone, increases endorphines - a horses natural pain killers For both : Relax Relieve Rejuvenate

```html
<!DOCTYPE html>
<html lang="en">
<head>
<meta charset="utf-8">
<title>Calm Reach Wellness – Business Card</title>
<link href="https://fonts.googleapis.com/css2?family=Open+Sans:wght@400;600&display=swap" rel="stylesheet">
<style>
  :root {
    --backdrop: #d9d4cd;
    --card-top: #f7f5f2;
    --card-top-edge: #e9e6e2;
    --band: #6e3b1f;
    --band-dark: #5a2f17;
    --silver-light: #f2f2f2;
    --silver-mid: #c9c9c9;
    --silver-dark: #9c9c9c;
    --brand: #6e3b1f;
    --text-light: #ffffff;
    --text-soft: #f1e4d8;
  }
  * { margin: 0; padding: 0; box-sizing: border-box; }
  html, body {
    width: 1200px; height: 768px; overflow: hidden;
    background: var(--backdrop);
    font-family: "Open Sans", Arial, sans-serif;
  }
  .canvas {
    position: relative; width: 1200px; height: 768px;
    display: flex; align-items: center; justify-content: center;
  }
  .card {
    position: relative; width: 1000px; height: 600px;
    background: linear-gradient(180deg, var(--card-top) 0%, var(--card-top-edge) 100%);
    border-radius: 10px; overflow: hidden;
    box-shadow: 0 12px 30px rgba(0,0,0,0.18);
  }
  .brand {
    position: absolute; top: 0; left: 0; right: 0; height: 320px;
    display: flex; align-items: center; justify-content: center;
    padding-top: 30px;
  }
  .brand-name {
    font-weight: 600; font-size: 50px; letter-spacing: 1px;
    color: var(--brand); white-space: nowrap;
  }
  .silver-line {
    position: absolute; left: 0; right: 0; height: 10px; top: 320px;
    background: linear-gradient(90deg, var(--silver-dark), var(--silver-light) 45%, var(--silver-mid) 75%, var(--silver-dark));
  }
  .band {
    position: absolute; left: 0; right: 0; top: 330px; height: 215px;
    background: linear-gradient(180deg, var(--band) 0%, var(--band-dark) 100%);
  }
  .notch {
    position: absolute; top: 0; left: 243px;
    width: 0; height: 0;
    border-left: 24px solid transparent; border-right: 24px solid transparent;
    border-top: 22px solid var(--card-top-edge);
  }
  .person {
    position: absolute; left: 60px; width: 420px; top: 40px;
    text-align: center; color: var(--text-light);
  }
  .person-name { font-size: 28px; font-weight: 400; }
  .person-title { font-size: 17px; color: var(--text-soft); margin-top: 6px; }
  .divider {
    position: absolute; left: 500px; top: 28px; bottom: 28px; width: 1px;
    background: rgba(255,255,255,0.55);
  }
  .contacts {
    position: absolute; left: 528px; top: 34px; list-style: none;
  }
  .contacts li {
    display: flex; align-items: center; gap: 14px;
    color: var(--text-light); font-size: 19px; height: 38px; white-space: nowrap;
  }
  .contacts svg { width: 24px; height: 24px; flex: none; }
  .silver-strip {
    position: absolute; left: 0; right: 0; top: 545px; bottom: 0;
    background: linear-gradient(180deg, var(--silver-mid) 0%, var(--silver-light) 40%, var(--silver-mid) 80%, var(--silver-dark) 100%);
  }
</style>
</head>
<body>
<div class="canvas">
  <div class="card">
    <div class="brand">
      <div class="brand-name">Calm Reach Wellness</div>
    </div>

    <div class="silver-line"></div>

    <div class="band">
      <div class="notch"></div>
      <div class="person">
        <div class="person-name">Marla Kessin</div>
        <div class="person-title">Certified Massage Therapist</div>
      </div>
      <div class="divider"></div>
      <ul class="contacts">
        <li>
          <svg viewBox="0 0 24 24"><circle cx="12" cy="12" r="12" fill="#fff"/><path d="M12 5a4.5 4.5 0 0 0-4.5 4.5c0 3.4 4.5 9 4.5 9s4.5-5.6 4.5-9A4.5 4.5 0 0 0 12 5zm0 6.3a1.8 1.8 0 1 1 0-3.6 1.8 1.8 0 0 1 0 3.6z" fill="#6e3b1f"/></svg>
          P.O. Box 871, Auburn, CA 95718
        </li>
        <li>
          <svg viewBox="0 0 24 24"><circle cx="12" cy="12" r="12" fill="#fff"/><path d="M8.6 6.2l1.9-.3 1.1 3-1.3 1a8 8 0 0 0 3.8 3.8l1-1.3 3 1.1-.3 1.9c-.2.8-1 1.3-1.8 1.2A10.5 10.5 0 0 1 7.4 8c-.1-.8.4-1.6 1.2-1.8z" fill="#6e3b1f"/></svg>
          530-555-0147
        </li>
        <li>
          <svg viewBox="0 0 24 24"><circle cx="12" cy="12" r="12" fill="#fff"/><rect x="6" y="8" width="12" height="8.5" rx="1" fill="none" stroke="#6e3b1f" stroke-width="1.6"/><path d="M6.5 8.6L12 13l5.5-4.4" fill="none" stroke="#6e3b1f" stroke-width="1.6"/></svg>
          marlakessin@quillpost.net
        </li>
        <li>
          <svg viewBox="0 0 24 24"><circle cx="12" cy="12" r="12" fill="#fff"/><circle cx="12" cy="12" r="6" fill="none" stroke="#6e3b1f" stroke-width="1.5"/><ellipse cx="12" cy="12" rx="2.6" ry="6" fill="none" stroke="#6e3b1f" stroke-width="1.3"/><path d="M6 12h12" stroke="#6e3b1f" stroke-width="1.3"/></svg>
          www.calmreachwellness.com
        </li>
      </ul>
    </div>

    <div class="silver-strip"></div>
  </div>
</div>
</body>
</html>
```